Schönheitssalon benötigt Flyer
Sehr schöne Arbeit, perfekt den Kundengeschmack getroffen. Leider zusätzliche Kosten durch (nicht enthaltene) Stockphotos, aber der Flyer ist sehr schick.
Zielgruppe
Ein Schönheitssalon in einer Pafümerie bietet diverse Angebote im Paket an (Gesichtsreinigung, Massage, Peeling, Maniküre, Sugaring). Vorrangig sollen Frauen angesprochen werden.
Aufgabenstellung
Faltblatt, gefalzt auf DIN A6 , 4-seiter
Endformat: 21,0 cm x 14,85 cm
gefalztes Endformat: 10,5 cm x 14,85 cm
Wir wünschen uns eine freundliche und helle Gestaltung mit rosé, voilett, pastell.
Das Grau, was jetzt gerade hinter dem Logo ist, wirkt sehr altbacken und nicht zeitgemäß.

```html
<!DOCTYPE html>
<html lang="de">
<head>
<meta charset="utf-8">
<title>Zartmoment – Faltblatt</title>
<link href="https://fonts.googleapis.com/css2?family=Quicksand:wght@400;500;700&family=Great+Vibes&display=swap" rel="stylesheet">
<style>
  :root{
    --stage:#f1eef0;
    --paper-a:#f8cfe4;
    --paper-b:#fce9f3;
    --pink:#e4579a;
    --pink-soft:#ee8cbb;
    --text:#6d6468;
    --band:#f08cbf;
    --white:#ffffff;
  }
  *{margin:0;padding:0;box-sizing:border-box}
  html,body{width:1200px;height:3600px;overflow:hidden}
  body{background:var(--stage);font-family:"Quicksand",sans-serif;color:var(--text);position:relative}
  .spread{position:absolute;left:40px;width:1120px;height:792px;overflow:hidden;
    background:linear-gradient(120deg,var(--paper-a),var(--paper-b) 55%,var(--paper-a));
    box-shadow:0 6px 18px rgba(0,0,0,.18)}
  .spread--outside{top:600px}
  .spread--inside{top:1560px}
  .swirl{position:absolute;inset:0;width:100%;height:100%}
  .panel{position:absolute;top:0;height:100%;width:560px}
  .panel--left{left:0}.panel--right{left:560px}

  /* outside, back panel */
  .intro{position:absolute;top:56px;left:60px;width:440px;text-align:center;color:var(--pink)}
  .intro h2{font-size:19px;font-weight:700;line-height:1.4;margin-bottom:24px}
  .intro p{font-size:18px;line-height:1.45}
  .intro .greet{margin-top:26px}
  .intro .signature{font-family:"Great Vibes",cursive;font-size:36px;color:#d8a7bf;margin-top:4px}
  .portrait{position:absolute;left:195px;top:420px;width:170px;height:170px;border-radius:50%;
    border:6px solid var(--white);background:radial-gradient(circle at 50% 40%,#f3e2d6,#d9d2d6 70%)}
  .contact{position:absolute;left:60px;width:440px;top:612px;text-align:center;color:var(--pink);font-size:17px;line-height:1.4}
  .contact .hours{margin-top:18px}

  /* outside, cover */
  .brand{position:absolute;top:70px;right:60px;width:320px;text-align:center}
  .brand__mark{width:22px;height:22px;border-radius:50%;border:2px solid var(--pink-soft);margin:0 auto 8px}
  .brand__name{font-size:40px;font-weight:500;color:var(--pink);line-height:1}
  .brand__tag{font-family:"Great Vibes",cursive;font-size:38px;color:#c9a3b7;position:absolute;top:160px;right:60px;width:380px;text-align:center}
  .cover-photo{position:absolute;right:0;top:270px;width:520px;height:522px;border-radius:58% 0 0 0;
    background:radial-gradient(circle at 55% 45%,#f0cdb8,#d7a794 45%,#6e4e44 80%)}
  .cover-strip{position:absolute;right:0;bottom:0;width:560px;height:96px;background:rgba(255,240,247,.88)}
  .cover-address{position:absolute;left:30px;bottom:18px;font-size:16px;line-height:1.35;color:var(--pink-soft)}
  .partner{position:absolute;right:30px;bottom:22px;text-align:right}
  .partner small{display:block;font-size:15px;color:var(--pink)}
  .partner span{font-size:24px;font-weight:500;color:#8a8488}

  /* inside */
  .pricelist{position:absolute;top:50px}
  .pricelist--face{left:44px;width:470px}
  .pricelist--extra{left:594px;width:480px}
  .pricelist h3{font-size:23px;font-weight:500;letter-spacing:2px;color:var(--pink);margin-bottom:24px;text-transform:uppercase}
  .treatment{margin-bottom:26px}
  .treatment__head{display:grid;grid-template-columns:1fr 105px 60px;font-size:16px;color:var(--pink-soft);white-space:nowrap}
  .treatment__head b{font-weight:500}
  .treatment__head span:last-child{text-align:right}
  .treatment p{font-size:13.5px;line-height:1.4;margin-top:3px}
  .rows{font-size:14.5px;line-height:1.45}
  .row{display:grid;grid-template-columns:1fr 70px 60px}
  .row span:nth-child(n+2){color:var(--pink-soft);text-align:right}
  .row--head span{font-size:12px}
  .sugaring{margin-top:28px}
  .band{position:absolute;left:0;bottom:0;width:100%;height:180px}
  .band__label{position:absolute;left:44px;bottom:32px;color:var(--white);font-weight:700;font-size:15px;letter-spacing:1.5px;text-transform:uppercase}
  .inside-photo{position:absolute;right:0;bottom:0;width:360px;height:170px;
    background:linear-gradient(100deg,#f3c9da,#efc4b1 50%,#f6d8e6);border-top-left-radius:120px 80px}
</style>
</head>
<body>

<section class="spread spread--outside">
  <svg class="swirl" viewBox="0 0 1120 792" preserveAspectRatio="none" aria-hidden="true">
    <path d="M0 120 C200 20 380 260 560 160 S900 0 1120 80 V0 H0Z" fill="#ffffff" opacity=".25"/>
    <path d="M0 520 C180 420 300 700 560 600 S900 420 1120 520" stroke="#ffffff" stroke-width="60" fill="none" opacity=".22"/>
    <path d="M560 0 C620 200 760 260 1120 220" stroke="#ffffff" stroke-width="40" fill="none" opacity=".2"/>
  </svg>

  <div class="panel panel--left">
    <div class="intro">
      <h2>Professionelle Kosmetikbehandlung<br>auf höchsten Niveau</h2>
      <p>Ich erstelle Ihnen gerne ein auf Sie persönlich abgestimmtes Kosmetikprogramm – natürlich mit hochwertigen Produkten, die Ihre Haut verwöhnen. Sie dürfen einfach nur genießen.</p>
      <p class="greet">Ich freue mich auf Sie !<br>Ihre</p>
      <p class="signature">Lena Marwitz</p>
    </div>
    <div class="portrait" role="img" aria-label="Porträtfoto der Kosmetikerin"></div>
    <div class="contact">
      <p>Rosenweg 12 | 40210 Musterstadt</p>
      <p class="hours">Öffnungszeiten<br>Do.: 9.30 – 19.00 Uhr<br>Fr.: 9.30 – 19.00 Uhr</p>
    </div>
  </div>

  <div class="panel panel--right">
    <div class="brand">
      <div class="brand__mark"></div>
      <div class="brand__name">Zartmoment</div>
    </div>
    <div class="brand__tag">Entspannung &amp; Kosmetik</div>
    <div class="cover-photo" role="img" aria-label="Foto einer entspannten Frau bei der Massage"></div>
    <div class="cover-strip">
      <p class="cover-address">Lena Marwitz<br>Rosenweg 12<br>40210 Musterstadt</p>
      <p class="partner"><small>im Hause der</small><span>Parfümerie Lindenhof</span></p>
    </div>
  </div>
</section>

<section class="spread spread--inside">
  <svg class="swirl" viewBox="0 0 1120 792" preserveAspectRatio="none" aria-hidden="true">
    <path d="M0 300 C250 200 400 420 700 340 S1000 260 1120 320" stroke="#ffffff" stroke-width="70" fill="none" opacity=".18"/>
  </svg>

  <div class="pricelist pricelist--face">
    <h3>Gesichtsbehandlungen</h3>
    <div class="treatment">
      <div class="treatment__head"><b>Reinigungs-Behandlung</b><span>ca. 60 Min.</span><span>35,- €</span></div>
      <p>Reinigung, Peeling, Ausreinigung, Maske &amp; Abschlusspflege</p>
    </div>
    <div class="treatment">
      <div class="treatment__head"><b>Intensiv-Behandlung</b><span>ca. 90 Min.</span><span>59,- €</span></div>
      <p>Reinigung, Peeling, Ausreinigung, Augenbrauen-Korrektur, Ampulle, Massage, Maske &amp; Abschlusspflege, leichtes Make-Up auf Wunsch</p>
    </div>
    <div class="treatment">
      <div class="treatment__head"><b>Verwöhn-Behandlung</b><span>ca. 90 Min.</span><span>67,- €</span></div>
      <p>Reinigung, Peeling, Ausreinigung, Augenbrauen-Korrektur, Ampulle, Massage, Maske, Hals- &amp; Dekolleté-Behandlung, leichtes Make-Up auf Wunsch</p>
    </div>
    <div class="treatment">
      <div class="treatment__head"><b>Luxus-Behandlung</b><span>ca. 120 Min.</span><span>81,- €</span></div>
      <p>Reinigung, Peeling, Ausreinigung, Augenbrauen-Korrektur, Ampulle, Massage, Vlies-Maske, Augenmaske, Lippenpackung, Handmassage &amp; Hals- &amp; Dekolleté-Behandlung, leichtes Make-Up auf Wunsch</p>
    </div>
    <div class="treatment">
      <div class="treatment__head"><b>Teenie-Behandlung (bis 18 Jahre)</b><span>ca. 60 Min.</span><span>28,- €</span></div>
      <p>Reinigung, Peeling, Ausreinigung &amp; Maske</p>
    </div>
  </div>

  <div class="pricelist pricelist--extra">
    <h3>Zusatz- &amp; Einzelbehandlungen</h3>
    <div class="rows">
      <div class="row row--head"><span></span><span>zusätzlich</span><span>einzeln</span></div>
      <div class="row"><span>Augenbrauen zupfen/wachsen</span><span></span><span>8,- €</span></div>
      <div class="row"><span>Augenbrauen färben</span><span>6,50 €</span><span>8,50 €</span></div>
      <div class="row"><span>Wimpern färben</span><span>7,- €</span><span>9,- €</span></div>
      <div class="row"><span>Augenbrauen &amp; Wimpern färben + zupfen</span><span></span><span>21,- €</span></div>
      <div class="row"><span>Wimpernwelle</span><span>32,- €</span><span>32,- €</span></div>
      <div class="row"><span>Pflegende Maniküre (60 Min.)</span><span>16,- €</span><span>26,- €</span></div>
      <div class="row"><span>Pflegende Maniküre + Lack</span><span>24,- €</span><span>32,- €</span></div>
      <div class="row"><span>Wirkstoffampulle</span><span></span><span>9,- €</span></div>
      <div class="row"><span>Tages-Make-Up</span><span></span><span>15,- €</span></div>
      <div class="row"><span>Abend- / Foto-Make-Up</span><span></span><span>25,- €</span></div>
      <div class="row"><span>Braut-Make-Up (inkl. Probe)</span><span></span><span>79,- €</span></div>
      <div class="row"><span>Klassische Rückenmassage ca. 30 Min.</span><span></span><span>25,- €</span></div>
    </div>
    <h3 class="sugaring">Sugaring</h3>
    <div class="rows">
      <div class="row"><span>Oberlippe</span><span>9,- €</span><span></span></div>
      <div class="row"><span>Oberlippe + Kinn</span><span>14,- €</span><span></span></div>
      <div class="row"><span>Arme</span><span>ab 25,- €</span><span></span></div>
      <div class="row"><span>Beine Unterschenkel</span><span>23,- €</span><span></span></div>
      <div class="row"><span>Beine komplett</span><span>39,- €</span><span></span></div>
      <div class="row"><span>Rücken</span><span>ab 25,- €</span><span></span></div>
    </div>
  </div>

  <svg class="band" viewBox="0 0 1120 180" preserveAspectRatio="none" aria-hidden="true">
    <path d="M0 60 C300 150 620 0 1120 40 V180 H0Z" fill="#ffffff" opacity=".55"/>
    <path d="M0 110 C320 170 640 60 1120 100 V180 H0Z" fill="var(--band)"/>
  </svg>
  <div class="inside-photo" role="img" aria-label="Foto einer Gesichtsmassage mit Blüten"></div>
  <p class="band__label">Andere Bereiche auf Anfrage!</p>
</section>

</body>
</html>
```